Agriculture Security Company needs a business card design

We need a business card design for a new company based in Seattle calls Fernwick Guardline LLC. We provide high-end physical security solutions that is geared and focused towards to the marijuana grow operations, wholesalers and distributors. We DO NOT get involved in the retail operations (store fronts). We would like to see designs that incorporate professionalism, reliability, trustworthy and forward thinking as traits of our organization.

Industry/Entity Type

Security

```html
<!DOCTYPE html>
<html lang="en">
<head>
<meta charset="utf-8">
<title>Fernwick Guardline LLC — Business Card</title>
<link rel="stylesheet" href="https://fonts.googleapis.com/css2?family=Open+Sans:wght@400;600;700&display=swap">
<style>
  :root {
    --bg: #e9e6e0;
    --card: #ffffff;
    --green-dark: #1f7a3c;
    --green-mid: #2c8c46;
    --green-light: #8dbb45;
    --blue: #5b93c8;
    --ink: #333333;
    --shadow: rgba(0, 0, 0, 0.18);
  }
  * { box-sizing: border-box; margin: 0; padding: 0; }
  html, body {
    width: 1200px; height: 1023px; overflow: hidden;
    background: var(--bg);
    font-family: "Open Sans", Arial, sans-serif;
  }
  .canvas { position: relative; width: 1200px; height: 1023px; }
  .card {
    position: absolute; width: 560px; height: 320px;
    background: var(--card);
    box-shadow: 0 10px 28px var(--shadow);
    overflow: hidden;
  }
  .card--front { left: 90px; top: 150px; }
  .card--back { left: 550px; top: 560px; }

  .wave { position: absolute; inset: 0; width: 100%; height: 100%; }

  .brand {
    display: flex; align-items: center; gap: 10px;
    color: var(--green-mid); font-weight: 700;
  }
  .brand__dot {
    width: 16px; height: 16px; border-radius: 50%;
    background: var(--green-light);
  }
  .card--front .brand { position: absolute; left: 44px; top: 96px; font-size: 38px; }

  .person { position: absolute; right: 34px; top: 28px; text-align: right; }
  .person__name { color: var(--green-mid); font-weight: 700; font-size: 22px; }
  .person__title { color: var(--green-light); font-size: 12px; }

  .address {
    position: absolute; right: 34px; top: 94px; text-align: right;
    color: var(--ink); font-size: 12px; line-height: 1.5;
    font-style: normal;
  }

  .contact {
    position: absolute; left: 44px; top: 190px;
    list-style: none; color: var(--ink); font-size: 12px; line-height: 1.7;
  }
  .contact li { display: flex; align-items: center; gap: 8px; }
  .contact svg { width: 11px; height: 11px; fill: var(--green-mid); }

  .company {
    position: absolute; right: 30px; bottom: 26px;
    color: #ffffff; font-size: 16px; font-weight: 600;
  }

  .card--back .website {
    position: absolute; top: 30px; left: 0; right: 0; text-align: center;
    color: var(--green-mid); font-size: 14px; letter-spacing: 0.22em;
  }
  .card--back .brand {
    position: absolute; left: 0; right: 0; top: 128px;
    justify-content: center; font-size: 48px;
  }
</style>
</head>
<body>
<main class="canvas">

  <section class="card card--front" aria-label="Business card front">
    <svg class="wave" viewBox="0 0 560 320" preserveAspectRatio="none" aria-hidden="true">
      <path d="M560,146 C450,152 400,206 356,250 C310,292 220,308 110,320 L560,320 Z" fill="var(--green-light)"/>
      <path d="M560,157 C456,163 408,214 364,257 C318,298 230,312 130,320 L560,320 Z" fill="#ffffff"/>
      <path d="M560,163 C460,169 414,220 370,262 C324,302 236,314 140,320 L560,320 Z" fill="var(--green-dark)"/>
      <path d="M0,318 C120,314 230,298 300,250 C250,296 150,312 0,320 Z" fill="var(--blue)"/>
    </svg>

    <div class="person">
      <p class="person__name">Dana Whitlow</p>
      <p class="person__title">President</p>
    </div>

    <address class="address">
      2180 Harbor Crest Ave<br>
      Seattle, WA 98121
    </address>

    <div class="brand"><span class="brand__dot"></span>Fernwick</div>

    <ul class="contact">
      <li><svg viewBox="0 0 24 24"><path d="M6.6 10.8a15 15 0 0 0 6.6 6.6l2.2-2.2a1 1 0 0 1 1-.25 11.4 11.4 0 0 0 3.6.57 1 1 0 0 1 1 1V20a1 1 0 0 1-1 1A17 17 0 0 1 3 4a1 1 0 0 1 1-1h3.5a1 1 0 0 1 1 1c0 1.250.2 2.450.57 3.6a1 1 0 0 1-.25 1z"/></svg>555-014-2287</li>
      <li><svg viewBox="0 0 24 24"><path d="M2 5h20v14H2z M2 5l10 8 10-8" stroke="#fff" stroke-width="1.5"/></svg>info@fernwickguardline.com</li>
      <li><svg viewBox="0 0 24 24"><circle cx="12" cy="12" r="10"/></svg>www.fernwickguardline.com</li>
    </ul>

    <p class="company">Fernwick Guardline LLC</p>
  </section>

  <section class="card card--back" aria-label="Business card back">
    <p class="website">www.fernwickguardline.com</p>
    <div class="brand"><span class="brand__dot"></span>Fernwick</div>
  </section>

</main>
</body>
</html>
```